Luxury Skincare Product Box Packaging Design

Vorabelle is a range of skincare products that help protect, nourish, and strengthen even the most sensitive skin, ensuring it is healthy, glowing, calm, and soft. Skincare practices support skin to enhance its appearance and relieve skin conditions. Your skin reflects your health. It is your body canvas and is an asset. The products contain naturally derived ingredients, aromatherapy oils, sustainable and ethical ingredients, organic ingredients where possible, natural preservatives and Australian oils, fruits, and extracts.

Vorabelle
Tagline is "Where Calm Finds Bloom"

Our products do not contain sulphates, parabens, phthalates, petrochemicals, synthetic colours, nor synthetic fragrances.

Everything about the Vorabelle Skincare name is creative and communicates luxury. Vorabelle from your first glance of the name, you will know that this is a company with excellent products.

By keeping it simple, unique, and elegant is often associated with high quality and is a way to establish trust. Vorabelle is a product that is “pure” and natural, so Vorabelle packaging would look simple, elegant, and clean.

I have uploaded the actual logo design and individual labels for the current skincare range I currently with the ingredients included so you can get an understanding of what I like. I have also added samples of package designs I quite like to assist with your designs.

Each Product box packaging sizes are as follows:

Product One - Exfoliating Herbs: 110mm (H) x 33mm Diameter
Product Two - Probiotic Lotion: 138mm (H) x 33mm Diameter
Product Three - Vitamin A Serum: 120mm (H) x 30mm Diameter
Updates

The Measurements are as follows: Product One: 110mm (H) x 33mm Diameter Product Two: 138mm (H) x 33mm Diameter Product Three: 120mm (H) x 30mm Diameter

Target Market(s)

Women

Requirements
Must have
• Logo, Product Name and ingredients and if you can barcode on the packaging that is the box design I am after
Nice to have
• samples of designs I like but open to suggestions

```html
<!DOCTYPE html>
<html lang="en">
<head>
<meta charset="utf-8">
<title>Vorabelle Vitamin A Serum – Box Front</title>
<link rel="stylesheet" href="https://fonts.googleapis.com/css2?family=Jost:wght@300;400;500;600&family=Libre+Baskerville:ital@0;1&display=swap">
<style>
  :root {
    --page: #ffffff;
    --mint: #c6e4da;
    --ink: #1d1d1b;
    --ink-soft: #2c2c2a;
    --copper: #b98466;
    --copper-light: #e9c2a8;
    --copper-dark: #8f5a40;
  }
  html, body {
    margin: 0;
    padding: 0;
    width: 802px;
    height: 1200px;
    overflow: hidden;
    background: var(--page);
  }
  .canvas {
    position: relative;
    width: 802px;
    height: 1200px;
  }
  .box-front {
    position: absolute;
    left: 297px;
    top: 178px;
    width: 232px;
    height: 912px;
    background: var(--mint);
    overflow: hidden;
  }
  .brand-name {
    position: absolute;
    left: 116px;
    top: 260px;
    transform: translate(-50%, -50%) rotate(-90deg);
    white-space: nowrap;
    font-family: "Jost", sans-serif;
    font-weight: 300;
    font-size: 66px;
    letter-spacing: 6px;
    color: var(--copper);
  }
  .product-title {
    position: absolute;
    left: 0;
    right: 0;
    top: 516px;
    text-align: center;
    font-family: "Jost", sans-serif;
    color: var(--ink);
    margin: 0;
  }
  .product-title .line-type {
    display: block;
    font-weight: 400;
    font-size: 19px;
    letter-spacing: 1.5px;
  }
  .product-title .line-form {
    display: block;
    margin-top: 4px;
    font-weight: 600;
    font-size: 17px;
    letter-spacing: 5px;
  }
  .free-from {
    position: absolute;
    left: 0;
    right: 0;
    top: 644px;
    text-align: center;
    font-family: "Libre Baskerville", serif;
    font-style: italic;
    font-size: 10.5px;
    line-height: 17px;
    color: var(--ink-soft);
    margin: 0;
  }
  .divider {
    position: absolute;
    left: 96px;
    top: 758px;
    width: 40px;
    height: 1.5px;
    background: var(--ink);
  }
  .skin-types {
    position: absolute;
    left: 0;
    right: 0;
    top: 772px;
    text-align: center;
    font-family: "Libre Baskerville", serif;
    font-size: 13px;
    color: var(--ink-soft);
    margin: 0;
  }
  .volume {
    position: absolute;
    left: 0;
    right: 0;
    top: 828px;
    text-align: center;
    font-family: "Jost", sans-serif;
    font-weight: 400;
    font-size: 19px;
    color: var(--ink);
    margin: 0;
  }
  .foil-band {
    position: absolute;
    left: 0;
    right: 0;
    bottom: 0;
    height: 31px;
    background: linear-gradient(100deg, var(--copper-dark) 0%, var(--copper) 30%, var(--copper-light) 55%, var(--copper) 75%, var(--copper-dark) 100%);
  }
</style>
</head>
<body>
  <main class="canvas">
    <section class="box-front" aria-label="Vorabelle Vitamin A Serum box front panel">
      <div class="brand-name">Vorabelle</div>
      <h1 class="product-title">
        <span class="line-type">VITAMIN A</span>
        <span class="line-form">SERUM</span>
      </h1>
      <p class="free-from">No sulphates, parabens,<br>phthalates, petrochemicals,<br>synthetic colours<br>No synthetic fragrance</p>
      <div class="divider"></div>
      <p class="skin-types">All Skin Types</p>
      <p class="volume">30ml</p>
      <div class="foil-band"></div>
    </section>
  </main>
</body>
</html>
```